HIgh-end jewelry designer needs a business card design

I need a business card design for the ecclectic & rather expensive jewelry designs. My approach to my work is to combine very old jewelry offset with contemporary items. I enjoy the idea of legacy as well as repurposing finely crafted items that are not possible to create any longer. My desire is to celebrate the past in a contemporary & funky way. The name of my business is VELLORINE. I see my business card design as simple & yet enigmatic as possible. In the end... clean, simple & understated is the look I am after. Thank you for your consideration...

Target Market(s)

I will use this business card for the trade as well as customers

Industry/Entity Type

Business

Contact Information for Business Card

Marta Quorrin Owner/Designer 555-203-7718

Requirements
Must have
• Clean & simple sophisticated design using the word "Vellorinne" as the logo. I like the idea of a play on the word itself, perhaps even using different fonts (i.e.: a bold helvetica combined with a lovely script). I'm afraid to say more because I don't want to limit creative input. Gosh, sometimes it's ok to break the rules!
Nice to have
• In my mind, I have imagined this business card to be simple, using my company name "Vellorine" in a playful yet sophisticated manner. I believe that doing something beautifully simple can be a true challenge. I have imagined something with just black & white, however I am open to ideas... after all that's why I'm here!
Should not have
• As Mozart once said... "It has too many notes!" I know I'm being silly, but I don't want it to be complicated or overly ornate.

```html
<!DOCTYPE html>
<html lang="en">
<head>
<meta charset="utf-8">
<title>Vellorine — Business Card</title>
<link rel="stylesheet" href="https://fonts.googleapis.com/css2?family=Cinzel:wght@400&family=Questrial&display=swap">
<style>
  :root {
    --page-bg: #ffffff;
    --card-bg: #ffffff;
    --ink: #3a3a3a;
    --ink-soft: #4a4a4a;
    --facet-light: #f4f4f4;
    --facet-mid: #cfcfcf;
    --card-shadow: rgba(0, 0, 0, 0.55);
  }
  * { margin: 0; padding: 0; box-sizing: border-box; }
  html, body {
    width: 1200px;
    height: 960px;
    overflow: hidden;
    background: var(--page-bg);
  }
  .canvas {
    position: relative;
    width: 1200px;
    height: 960px;
  }
  .card {
    position: absolute;
    width: 582px;
    height: 331px;
    background: var(--card-bg);
    box-shadow: 8px 9px 10px var(--card-shadow);
    color: var(--ink);
    overflow: hidden;
  }
  .card--front { left: 296px; top: 73px; }
  .card--back  { left: 292px; top: 567px; height: 329px; }

  .gem-art {
    position: absolute;
    background: linear-gradient(180deg, var(--facet-mid) 0%, var(--facet-light) 100%);
  }
  .card--front .gem-art { left: 240px; top: 30px; width: 102px; height: 50px; }
  .card--back .gem-art--left  { left: 0;     top: 35px; width: 123px; height: 270px;
    background: linear-gradient(90deg, var(--facet-mid) 0%, var(--facet-light) 100%); }
  .card--back .gem-art--right { right: 0;    top: 35px; width: 124px; height: 270px;
    background: linear-gradient(270deg, var(--facet-mid) 0%, var(--facet-light) 100%); }

  .line {
    position: absolute;
    left: 0;
    width: 100%;
    text-align: center;
    white-space: nowrap;
    line-height: 1;
  }
  .wordmark,
  .holder-name,
  .holder-role {
    font-family: "Cinzel", serif;
    font-weight: 400;
  }
  .phone {
    font-family: "Questrial", sans-serif;
    color: var(--ink-soft);
  }

  /* front */
  .card--front .wordmark    { top: 90px;  font-size: 27px; letter-spacing: 1px; }
  .card--front .holder-name { top: 173px; font-size: 42px; }
  .card--front .holder-role { top: 221px; font-size: 25px; }
  .card--front .phone       { top: 270px; font-size: 20px; }

  /* back */
  .card--back .wordmark    { top: 68px;  font-size: 38px; letter-spacing: 1px; }
  .card--back .holder-name { top: 183px; font-size: 34px; }
  .card--back .holder-role { top: 219px; font-size: 19px; }
  .card--back .phone       { top: 253px; font-size: 15px; }
</style>
</head>
<body>
  <main class="canvas">
    <section class="card card--front" aria-label="Card front">
      <div class="gem-art" role="img" aria-label="Faceted gemstone line illustration above the company name"></div>
      <p class="line wordmark">VELLORINE</p>
      <p class="line holder-name">Marta Quorrin</p>
      <p class="line holder-role">Owner/Designer</p>
      <p class="line phone">555-203-7718</p>
    </section>

    <section class="card card--back" aria-label="Card back">
      <div class="gem-art gem-art--left" role="img" aria-label="Large faceted gemstone line illustration cropped at the left edge"></div>
      <div class="gem-art gem-art--right" role="img" aria-label="Large faceted gemstone line illustration cropped at the right edge"></div>
      <p class="line wordmark">VELLORINE</p>
      <p class="line holder-name">Marta Quorrin</p>
      <p class="line holder-role">Owner/Designer</p>
      <p class="line phone">555-203-7718</p>
    </section>
  </main>
</body>
</html>
```